Business Card for a Mortgage Agent (myself)

I need a business card for my new job as Mortgage Agent. The Broker's logo is to be on the card as well as the brokerage License number. Not sure if to include a photo or not. Info to be on card.
Dante Roux
Mortgage Agent
Lic # M47105386
Cell: 905-614-2753
Email: danterouxk.ma@fennmail.com
Web: www.karlvostermortgages.com
TPW Brokerage Lic. # 73918

```html
<!DOCTYPE html>
<html lang="en">
<head>
<meta charset="UTF-8">
<title>TPW Mortgage Agent Business Card</title>
<link href="https://fonts.googleapis.com/css2?family=Mulish:wght@400;600;800&display=swap" rel="stylesheet">
<style>
  :root {
    --backdrop: #9d9d9f;
    --navy: #22245a;
    --navy-deep: #1f2152;
    --gold: #e5b824;
    --paper: #eeeeee;
    --ink: #4a4a4f;
    --white: #ffffff;
  }
  * { margin: 0; padding: 0; box-sizing: border-box; }
  html, body {
    width: 1200px; height: 900px; overflow: hidden;
    background: var(--backdrop);
    font-family: "Mulish", Arial, sans-serif;
  }
  .card {
    position: absolute; left: 363px;
    width: 475px; height: 271px;
    overflow: hidden;
  }
  .card-front { top: 145px; background: var(--navy-deep); }
  .card-back { top: 484px; background: var(--paper); }

  /* front brand block */
  .brand-front {
    position: absolute; left: 0; top: 58px; width: 100%;
    text-align: center; color: var(--white);
  }
  .brand-front .brand-mark {
    display: inline-flex; align-items: center; gap: 14px;
  }
  .brand-front .brand-square {
    width: 44px; height: 44px; background: var(--gold);
  }
  .brand-front .brand-initials {
    font-weight: 800; font-size: 46px; letter-spacing: 14px; line-height: 1;
  }
  .brand-front .brand-name {
    margin-top: 18px; font-weight: 600; font-size: 13px; letter-spacing: 2.5px;
    text-transform: uppercase;
  }
  .brand-front .brand-licence {
    margin-top: 8px; font-size: 9px; font-weight: 600;
  }

  /* back */
  .agent-photo {
    position: absolute; left: 0; top: 24px; width: 192px; height: 247px;
    background: linear-gradient(180deg, #c99a83 0%, #8a7c7a 42%, #3a3b40 62%, #2c2d31 100%);
    border-radius: 90px 90px 0 0;
  }
  .swoosh { position: absolute; left: 0; top: 0; width: 475px; height: 271px; }

  .brand-back {
    position: absolute; left: 198px; top: 30px; width: 116px;
    text-align: center; color: var(--navy);
  }
  .brand-back .brand-mark { display: inline-flex; align-items: center; gap: 7px; }
  .brand-back .brand-square { width: 20px; height: 20px; background: var(--gold); }
  .brand-back .brand-initials { font-weight: 800; font-size: 20px; letter-spacing: 6px; line-height: 1; }
  .brand-back .brand-name {
    margin-top: 6px; font-weight: 600; font-size: 6px; letter-spacing: 1px;
    text-transform: uppercase;
  }
  .brand-back .brand-licence { margin-top: 2px; font-size: 4.5px; text-align: right; }

  .agent {
    position: absolute; left: 197px; top: 118px; color: var(--ink);
  }
  .agent-name { font-weight: 800; font-size: 16px; color: var(--navy); line-height: 1.1; }
  .agent-title { font-size: 10.5px; margin-top: 1px; }
  .contact-list { list-style: none; margin-top: 12px; font-size: 10px; line-height: 14px; }
  .contact-list li { display: flex; align-items: center; gap: 8px; }
  .contact-list svg { width: 9px; height: 9px; fill: var(--navy); }
  .licences { margin-top: 7px; font-size: 10px; line-height: 14px; }

  .website {
    position: absolute; right: 20px; top: 245px;
    color: var(--white); font-size: 10px; letter-spacing: 0.3px;
  }
</style>
</head>
<body>

<section class="card card-front">
  <div class="brand-front">
    <div class="brand-mark">
      <span class="brand-square"></span>
      <span class="brand-initials">TPW</span>
    </div>
    <p class="brand-name">True Path Wealth</p>
    <p class="brand-licence">License #73918</p>
  </div>
</section>

<section class="card card-back">
  <svg class="swoosh" viewBox="0 0 475 271" aria-hidden="true">
    <path d="M190 271 C300 250 410 210 475 160 L475 271 Z" fill="var(--navy)"/>
    <path d="M190 262 C290 250 360 232 405 210 C360 238 290 258 190 271 Z" fill="var(--gold)"/>
  </svg>

  <div class="agent-photo" role="img" aria-label="Portrait photo of the mortgage agent in a dark suit"></div>

  <div class="brand-back">
    <div class="brand-mark">
      <span class="brand-square"></span>
      <span class="brand-initials">TPW</span>
    </div>
    <p class="brand-name">True Path Wealth</p>
    <p class="brand-licence">License #73918</p>
  </div>

  <div class="agent">
    <h1 class="agent-name">Dante Roux</h1>
    <p class="agent-title">Mortgage Agent</p>
    <ul class="contact-list">
      <li>
        <svg viewBox="0 0 10 10" aria-hidden="true"><path d="M2.5 0h5a1 1 0 0 1 1 1v8a1 1 0 0 1-1 1h-5a1 1 0 0 1-1-1V1a1 1 0 0 1 1-1zm.6 1.2v6.6h3.8V1.2z"/></svg>
        905-614-2753
      </li>
      <li>
        <svg viewBox="0 0 10 10" aria-hidden="true"><path d="M0 2h10v6H0zM1 3l4 3 4-3v-.2H1z"/></svg>
        danterouxk.ma@fennmail.com
      </li>
    </ul>
    <p class="licences">Lic # M47105386<br>TPW Brokerage Lic. # 73918</p>
  </div>

  <p class="website">karlvostermortgages.com</p>
</section>

</body>
</html>
```